Design NEW business card

We would like a business card using the colour deep red wine or dark navy blue textured background (patterned or not, open to suggestions) with a high gloss debossed rose gold/copper MT Martin Tully Jewellery business name (Provided). I have included images for your review we would like to keep our currently logo and business name on the front but you can change the layout and positioning. For the back of the card we are open to all suggestions/variations.
Industry/Entity Type
Business
Contact Information for Business Card
Use our current MT Martin Tully Jewellery logo (Provided image)
Look and feel
Each slider illustrates characteristics of the customer's brand and the style your logo design should communicate.

```html
<!DOCTYPE html>
<html lang="en">
<head>
<meta charset="utf-8">
<title>Martin Tully Jewellery – Business Card</title>
<link rel="stylesheet" href="https://fonts.googleapis.com/css2?family=Montserrat:wght@400;500;700&display=swap">
<style>
  :root {
    --backdrop: #e8e8e8;
    --wine: #4a1518;
    --wine-deep: #3a0f12;
    --wine-light: #571c20;
    --copper: #b4683f;
    --copper-soft: #c98a62;
    --paper: #fbfbfa;
    --paper-pattern: #f1f1ef;
    --shadow: rgba(0, 0, 0, 0.18);
  }
  * { box-sizing: border-box; margin: 0; padding: 0; }
  html, body {
    width: 1200px;
    height: 805px;
    overflow: hidden;
    background: var(--backdrop);
    font-family: "Montserrat", sans-serif;
  }
  .canvas {
    position: relative;
    width: 1200px;
    height: 805px;
  }
  .card {
    position: absolute;
    width: 560px;
    height: 320px;
    border-radius: 30px;
    overflow: hidden;
    box-shadow: 0 14px 30px var(--shadow);
  }

  /* Back side: contact card */
  .card--contact {
    left: 560px;
    top: 70px;
    background: var(--paper);
  }
  .card--contact .paper-pattern {
    position: absolute;
    inset: 0;
    background: linear-gradient(135deg, var(--paper) 0%, var(--paper-pattern) 50%, var(--paper) 100%);
  }
  .contact-person {
    position: absolute;
    left: 40px;
    bottom: 60px;
    color: var(--copper);
  }
  .contact-person__name {
    font-weight: 700;
    font-size: 22px;
    letter-spacing: 0.5px;
    text-transform: uppercase;
  }
  .contact-person__role {
    font-weight: 500;
    font-size: 12px;
    letter-spacing: 1px;
    text-transform: uppercase;
    margin-top: 2px;
  }
  .contact-details {
    position: absolute;
    right: 36px;
    top: 120px;
    text-align: right;
    color: var(--copper);
    font-weight: 500;
    font-size: 10.5px;
    letter-spacing: 0.8px;
    line-height: 1.55;
    text-transform: uppercase;
  }
  .contact-details__web {
    margin-top: 10px;
    font-size: 11px;
  }

  /* Front side: brand card */
  .card--brand {
    left: 100px;
    top: 420px;
    background: var(--wine);
  }
  .card--brand .wine-texture {
    position: absolute;
    inset: 0;
    background: radial-gradient(ellipse at 40% 40%, var(--wine-light) 0%, var(--wine) 55%, var(--wine-deep) 100%);
  }
  .brand-name {
    position: absolute;
    left: 300px;
    top: 168px;
    color: var(--copper-soft);
    font-weight: 400;
    text-transform: uppercase;
  }
  .brand-name__main {
    font-size: 22px;
    letter-spacing: 6px;
  }
  .brand-name__sub {
    font-size: 9px;
    letter-spacing: 9px;
    margin-top: 4px;
  }
</style>
</head>
<body>
<main class="canvas">
  <section class="card card--contact" aria-label="Business card back">
    <div class="paper-pattern" role="img" aria-label="Faint nested diamond pattern printed on white card stock"></div>
    <div class="contact-details">
      <p>daniel@tullyjewellery.example</p>
      <p>+91 900-555-0142</p>
      <p class="contact-details__web">www.tullyjewellery.example</p>
    </div>
    <div class="contact-person">
      <p class="contact-person__name">Daniel Avery</p>
      <p class="contact-person__role">Co-Founder &amp; CEO</p>
    </div>
  </section>

  <section class="card card--brand" aria-label="Business card front">
    <div class="wine-texture" role="img" aria-label="Deep wine red fibrous paper texture"></div>
    <div class="brand-name">
      <p class="brand-name__main">Martin Tully</p>
      <p class="brand-name__sub">Jewellery</p>
    </div>
  </section>
</main>
</body>
</html>
```